Trucking company specializing in intermodal containers

We need a logo design for our trucking company based in Kent, Washington. Our companies name is Dorvale Haulworks LLC, we specialize in intermodal containers, and work off of the Crestmark rail lines and the ports. We provide service by transporting freight with our fleet of trucks. We operate within Washington, Oregon, and Idaho. Our fleet consists of an east division and a local division. Our team motto currently is globally connected, locally invested.

Target Market(s)

brokers, intermodal management companies, customers

Industry/Entity Type

Trucking Company

Contact Information for Business Card

physical address 4519 N. 163rd Pl Kent, WA 98517
office number is 253-614-9026

Font styles to use
Sans Serif

Colors

Designer to choose colors to be used in the design.

Requirements
Must have
• We need to update our current logo. Something like an emblem; that makes a statement that this logo/ sign represents Dorvale Haulworks. Something like a royal stamp but in this case a royal shield.
Nice to have
• simple, yet bold. something someone does not currently have. We need something fresh and exciting. Something that will also make a statement because currently our reputation is great within the industry and our community. But we need to reflect that we are professional and willing to provide the best service. We are open to new statement lines.
Should not have
• Should not have something thats been used before. We are open to suggestions that you have and a design that is completely unique and you make originally without what we want but what you like as well. Ofcourse it should still represent the industry we are in.

```html
<!DOCTYPE html>
<html lang="en">
<head>
<meta charset="utf-8">
<title>Dorvale Haulworks LLC — Business Card</title>
<link href="https://fonts.googleapis.com/css2?family=Montserrat:wght@400;500;600;700&display=swap" rel="stylesheet">
<style>
  :root {
    --bg: #262626;
    --orange: #f07a1f;
    --paper: #f4f4f4;
    --band-1: #2b2b2b;
    --band-2: #333333;
    --band-3: #3c3c3c;
    --band-4: #474747;
    --back: #404040;
    --white: #ffffff;
    --light: #e8e8e8;
  }
  * { box-sizing: border-box; margin: 0; padding: 0; }
  html, body { width: 857px; height: 1200px; overflow: hidden; }
  body {
    background: var(--bg);
    font-family: "Montserrat", sans-serif;
    position: relative;
  }
  .card {
    position: absolute;
    top: 282px;
    width: 380px;
    height: 636px;
    overflow: hidden;
  }
  .card--front { left: 32px; }
  .card--back { left: 445px; background: var(--back); }

  /* front: logo area */
  .brand-panel {
    position: absolute; left: 0; top: 0; width: 100%; height: 257px;
    background: var(--paper);
  }
  .side-bar {
    position: absolute; background: var(--orange);
  }
  .brand-panel .side-bar { top: 130px; height: 24px; width: 44px; }
  .brand-panel .side-bar--left { left: 0; }
  .brand-panel .side-bar--right { right: 0; }
  .brand-name {
    position: absolute;
    left: 60px; right: 60px;
    text-align: center;
    color: var(--orange);
    font-weight: 700;
    line-height: 1.05;
    letter-spacing: 0.5px;
  }
  .brand-panel .brand-name { top: 104px; font-size: 27px; }

  /* front: info bands */
  .band {
    position: absolute; left: 0; width: 100%;
    display: flex; align-items: center;
  }
  .band--name { top: 257px; height: 89px; background: var(--band-1); }
  .band--address { top: 346px; height: 91px; background: var(--band-2); }
  .band--phone { top: 437px; height: 90px; background: var(--band-3); }
  .band--web { top: 527px; height: 89px; background: var(--band-4); }
  .bottom-stripe {
    position: absolute; left: 0; bottom: 0; width: 100%; height: 20px;
    background: var(--orange);
  }

  .icon-ring {
    position: absolute;
    width: 46px; height: 46px;
    border: 2px solid var(--orange);
    border-radius: 50%;
    display: flex; align-items: center; justify-content: center;
  }
  .icon-ring svg { width: 22px; height: 22px; fill: var(--light); }
  .icon-ring--right { right: 32px; }
  .icon-ring--left { left: 42px; }

  .company-title {
    position: absolute; right: 96px; text-align: right;
  }
  .company-title__name {
    color: var(--white); font-weight: 700; font-size: 36px; letter-spacing: 1px; line-height: 1;
  }
  .company-title__tag {
    color: var(--orange); font-weight: 400; font-size: 13px; letter-spacing: 0.3px; margin-top: 2px;
  }

  .detail {
    position: absolute;
    color: var(--light);
    font-weight: 600;
    font-size: 16px;
    line-height: 1.35;
  }
  .band--address .detail { left: 118px; }
  .band--phone .detail { right: 106px; text-align: right; }
  .band--web .detail { left: 118px; font-size: 15.5px; }

  /* back */
  .card--back .side-bar { top: 233px; height: 131px; width: 20px; }
  .card--back .side-bar--left { left: 0; }
  .card--back .side-bar--right { right: 0; }
  .card--back .brand-name { top: 270px; left: 40px; right: 40px; font-size: 30px; }
  .back-tagline {
    position: absolute; bottom: 40px; left: 0; width: 100%;
    text-align: center; color: var(--orange); font-size: 20px; font-weight: 400; letter-spacing: 0.5px;
  }
</style>
</head>
<body>

<section class="card card--front" aria-label="Business card front">
  <div class="brand-panel">
    <span class="side-bar side-bar--left"></span>
    <span class="side-bar side-bar--right"></span>
    <div class="brand-name">DORVALE<br>HAULWORKS LLC</div>
  </div>

  <div class="band band--name">
    <div class="company-title">
      <div class="company-title__name">DORVALE</div>
      <div class="company-title__tag">TRACKING COMPANY</div>
    </div>
    <div class="icon-ring icon-ring--right">
      <svg viewBox="0 0 24 24" aria-hidden="true"><circle cx="12" cy="7" r="4.5"/><path d="M3 22c0-5 4-8.5 9-8.5s9 3.5 9 8.5z"/></svg>
    </div>
  </div>

  <div class="band band--address">
    <div class="icon-ring icon-ring--left">
      <svg viewBox="0 0 24 24" aria-hidden="true"><path d="M12 3 2 12h3v9h5v-6h4v6h5v-9h3z"/></svg>
    </div>
    <div class="detail">4519 N. 163rd<br>Pl Kent, WA</div>
  </div>

  <div class="band band--phone">
    <div class="detail">+253 - 614 - 9026<br>+253 - 614 - 9026</div>
    <div class="icon-ring icon-ring--right">
      <svg viewBox="0 0 24 24" aria-hidden="true"><path d="M3 8c0-2 2-3 4-3h10c2 0 4 1 4 3v2h-4V8H7v2H3z"/><path d="M6 12h12l2 8H4z"/></svg>
    </div>
  </div>

  <div class="band band--web">
    <div class="icon-ring icon-ring--left">
      <svg viewBox="0 0 24 24" aria-hidden="true" fill="none" stroke="#e8e8e8" stroke-width="1.6" style="fill:none"><circle cx="12" cy="12" r="9"/><ellipse cx="12" cy="12" rx="4" ry="9"/><path d="M3 12h18M5 7h14M5 17h14"/></svg>
    </div>
    <div class="detail">mail@dorvale.com<br>www.dorvalehaulworks.com</div>
  </div>

  <div class="bottom-stripe"></div>
</section>

<section class="card card--back" aria-label="Business card back">
  <span class="side-bar side-bar--left"></span>
  <span class="side-bar side-bar--right"></span>
  <div class="brand-name">DORVALE<br>HAULWORKS LLC</div>
  <div class="back-tagline">TRACKING COMPANY</div>
</section>

</body>
</html>
```